Banner Ads for Online Poker Promotion

We are an online poker network, the KRX (www.thekrx.eu). We are looking for a small selection of web banner ads for our latest promotion and we are trying crowdsourcing for the first time!

Banner sizes that we need are:
- 196x523 (static .psd and .png)
- 199x129 (static .psd and .png)
- 447x426 (static .psd and .png)
- 500x400 (static .psd and .png)
- 697x167 (static .psd and .png)
- 460x60 (animated .gif)

The promotion name is ‘Late Rush’ and the concept is that a person who enters one of the specified tournaments four or more times during the promotion will win a free ticket to play that tournament again. So effectively a ‘Rush Late, Bag a Seat’ promo. We also are giving away €10,000 in free entries to the tournaments during the promotion. The specific tournaments are called ‘Calm Dawn Out’ and ‘The Sun Deck’ and run daily on our network. The promotion runs October 1 – 31.

Guidelines:

The name of the promotion, ‘Late Rush’, should feature prominently in the banners.

The strap line can be ‘Rush Late, Bag a Seat’ or something that encourages players to ‘take a shot’ at the tournaments.

Our network logo may feature, but is not absolutely necessary.

Examples of past promotional imagery can be found on our website, in particular these pages: http://www.thekrx.eu/promotions/ and http://www.thekrx.eu/promotions/archived-promotions/

We are looking to go in a more modern and risqué direction than the past, in order to stand out from competition which is very bland.

Please do not use common poker imagery – so no cards, chips, suit icons etc – or objects associated with live poker (tables, etc). This sort of imagery is too clichéd.

More like iOS7, less like iOS6

Think glamour, neon, rock music, extreme sports, and the Soft Tide!

If any further guidance is needed please don’t hesitate to ask.

```html
<!DOCTYPE html>
<html lang="en">
<head>
<meta charset="UTF-8">
<title>Late Rush — Banner 500x400</title>
<link rel="stylesheet" href="https://fonts.googleapis.com/css2?family=Pacifico&family=Raleway:wght@300;600&display=swap">
<style>
  :root {
    --sky-top: #9aa2a6;
    --sky-mid: #7c868c;
    --city-low: #46505a;
    --city-deep: #2e363e;
    --title-white: #ffffff;
    --band-white: rgba(255, 255, 255, 0.62);
    --strap-ink: #3a3d40;
    --mark-white: rgba(255, 255, 255, 0.9);
  }

  html, body {
    margin: 0;
    padding: 0;
    width: 1200px;
    height: 960px;
    overflow: hidden;
    background: var(--city-deep);
  }

  .banner {
    position: relative;
    width: 1200px;
    height: 960px;
    overflow: hidden;
  }

  .banner__skyline {
    position: absolute;
    inset: 0;
    background:
      linear-gradient(180deg,
        var(--sky-top) 0%,
        var(--sky-mid) 30%,
        #5d676f 60%,
        var(--city-low) 80%,
        var(--city-deep) 100%);
  }

  .banner__title {
    position: absolute;
    left: 0;
    right: 0;
    top: 215px;
    margin: 0;
    text-align: center;
    font-family: "Pacifico", cursive;
    font-weight: 400;
    font-size: 176px;
    line-height: 1;
    color: var(--title-white);
    text-shadow: 0 4px 14px rgba(0, 0, 0, 0.25);
    z-index: 2;
  }

  .banner__band {
    position: absolute;
    left: 0;
    right: 0;
    top: 439px;
    height: 214px;
    background: var(--band-white);
    z-index: 1;
  }

  .banner__strap {
    position: absolute;
    left: 408px;
    top: 470px;
    margin: 0;
    font-family: "Raleway", sans-serif;
    font-weight: 300;
    font-size: 74px;
    line-height: 82px;
    color: var(--strap-ink);
    z-index: 2;
  }

  .banner__strap strong {
    font-weight: 600;
  }

  .banner__mark {
    position: absolute;
    left: 76px;
    bottom: 52px;
    font-family: "Raleway", sans-serif;
    font-weight: 300;
    font-size: 40px;
    letter-spacing: 2px;
    color: var(--mark-white);
    z-index: 2;
  }
</style>
</head>
<body>
  <main class="banner">
    <div class="banner__skyline" role="img" aria-label="Hazy, muted photograph of a city skyline with tall skyscrapers"></div>
    <h1 class="banner__title">Late Rush</h1>
    <div class="banner__band"></div>
    <p class="banner__strap">Rush <strong>Late</strong><br>Bag a <strong>Seat</strong></p>
    <div class="banner__mark">KRX</div>
  </main>
</body>
</html>
```